Flyer Design Project

We are a Human Resources and payroll company with a dedicated staffing and recruiting division. We need a really professional looking and creative flyer that breifly explains our offerings. This flyer will be given to other sales people that sell complementary services to what we offer. Those salespeople will to leave this flyer with prospective clients that want services that do not offer and we do.
Updates

I just uploades our logo in EPS!  Thank you!

Target Market(s)

Employers are our target market. Mostly healthcare but not exclusively.

Industry/Entity Type

It Company

Requirements
Must have
• Photos of people in a working environment would be good. All offering in attached files must be in the flyer as well as our logo.
Nice to have
• It would be nice to convey that we care about our clients and their employees.

```html
<!DOCTYPE html>
<html lang="en">
<head>
<meta charset="utf-8">
<title>Recruiting and Staffing Packages Flyer</title>
<link href="https://fonts.googleapis.com/css2?family=Ubuntu:wght@400;500&display=swap" rel="stylesheet">
<style>
  :root {
    --page-bg: #e4e5e7;
    --sheet-bg: #f2f2f3;
    --brand-blue: #2f6db5;
    --brand-blue-dark: #24579a;
    --charcoal: #3a3a3c;
    --charcoal-deep: #262628;
    --card-bg: #dcdcde;
    --card-bg-light: #e6e6e8;
    --text: #3b3b3d;
    --white: #ffffff;
  }
  * { box-sizing: border-box; margin: 0; padding: 0; }
  html, body { width: 1200px; height: 1000px; overflow: hidden; }
  body {
    background: var(--page-bg);
    font-family: "Ubuntu", Arial, sans-serif;
    color: var(--text);
    position: relative;
  }
  .flyer {
    position: absolute;
    left: 270px; top: 33px;
    width: 660px; height: 934px;
    background: var(--sheet-bg);
    box-shadow: 0 4px 18px rgba(0,0,0,.18);
    overflow: hidden;
  }
  .top-band {
    position: absolute; left: 0; top: 16px;
    width: 380px; height: 14px;
    background: var(--brand-blue);
    clip-path: polygon(0 0, 100% 0, 97% 100%, 0 100%);
  }
  .hero-photo {
    position: absolute; left: 0; top: 0;
    width: 660px; height: 390px;
    clip-path: polygon(400px 0, 660px 0, 660px 390px, 250px 390px, 150px 290px);
    background: linear-gradient(160deg, #e9ecef 0%, #cfd3d8 35%, #7c8a7a 60%, #b9bcc0 100%);
  }
  .brand {
    position: absolute; left: 56px; top: 70px;
    width: 200px; text-align: center;
  }
  .brand-mark {
    width: 62px; height: 62px; margin: 0 auto 10px;
    border: 3px solid var(--charcoal-deep); border-radius: 50%;
  }
  .brand-name { font-size: 17px; font-weight: 500; color: var(--charcoal-deep); }
  .title-panel {
    position: absolute; left: 0; top: 250px;
    width: 310px; height: 140px;
    background: linear-gradient(180deg, var(--charcoal) 0%, var(--charcoal-deep) 100%);
    clip-path: polygon(0 12px, 135px 0, 310px 140px, 0 140px);
  }
  .title-panel h1 {
    position: absolute; left: 50px; top: 72px;
    font-size: 21px; font-weight: 400; line-height: 1.2; color: var(--white);
  }
  .packages {
    position: absolute; left: 40px; top: 400px;
    width: 584px;
  }
  .package-row {
    display: flex; gap: 10px; align-items: flex-start;
  }
  .package {
    position: relative;
    background: linear-gradient(180deg, var(--card-bg-light), var(--card-bg));
    padding: 40px 12px 10px;
    font-size: 9.5px; line-height: 1.3;
  }
  .package p { margin-bottom: 3px; }
  .package-tab {
    position: absolute; left: 0; top: 0;
    height: 26px; padding: 0 12px;
    background: var(--brand-blue);
    color: var(--white); font-size: 13px; font-weight: 500;
    line-height: 26px; white-space: nowrap;
  }
  .package-tab::after {
    content: ""; position: absolute; left: 12px; bottom: -9px;
    border-left: 9px solid transparent; border-right: 9px solid transparent;
    border-top: 9px solid var(--brand-blue-dark);
  }
  .package-tab .sep { margin: 0 8px; }
  .package-row .package { width: 188px; }
  .package-row .package-tab { width: 164px; }
  .package-a { margin-top: 20px; }
  .package-b { margin-top: 10px; }
  .package-c { margin-top: 0; }
  .team-photo {
    margin-top: 8px; width: 164px; height: 84px;
    background: linear-gradient(180deg, #a9c59a 0%, #5a6470 60%, #2d3440 100%);
  }
  .package-d { margin-top: 12px; width: 584px; padding-top: 38px; }
  .package-d .package-tab { width: 520px; }
  .footer {
    position: absolute; left: 0; bottom: 14px;
    width: 660px; height: 30px;
    background: var(--charcoal-deep);
    color: #d9d9db; font-size: 9.5px;
    display: flex; align-items: center; justify-content: space-between;
    padding: 0 24px; white-space: nowrap;
  }
  .footer-item { display: flex; align-items: center; gap: 6px; white-space: nowrap; }
  .footer-item svg { width: 11px; height: 11px; flex: none; }
</style>
</head>
<body>
  <div class="flyer">
    <div class="hero-photo" role="img" aria-label="Photo of three colleagues reviewing a document together in a bright office"></div>
    <div class="top-band"></div>

    <div class="brand">
      <div class="brand-mark"></div>
      <div class="brand-name">Your Logo goes Here</div>
    </div>

    <div class="title-panel">
      <h1>Recruiting and<br>Staffing Packages</h1>
    </div>

    <div class="packages">
      <div class="package-row">
        <section class="package package-a">
          <div class="package-tab">Package A<span class="sep">|</span>$275.00</div>
          <p>Source up to 6 resumes</p>
          <p>Position is advertised on 1 job board</p>
          <p>Note: Job Description is provided by client. We can provide this service to you for an additional fee of $35)</p>
          <div class="team-photo" role="img" aria-label="Photo of a smiling business team standing outdoors"></div>
        </section>

        <section class="package package-b">
          <div class="package-tab">Package B<span class="sep">|</span>$390.00</div>
          <p>Source up to 8 resumes</p>
          <p>Position advertised on 2 job boards</p>
          <p>Phone screen prospective candidates utilizing position specific requirements and questions provided by Client</p>
          <p>Client will be presented with a summarization of phone screen along with prospective candidates resume</p>
          <p>Note: Job Description is provided by client. We can provide this service to you for an additional fee of $35)</p>
        </section>

        <section class="package package-c">
          <div class="package-tab">Package C<span class="sep">|</span>$625.00</div>
          <p>Source up to 10 resumes</p>
          <p>Create a customized job description that best fits your organizations needs</p>
          <p>Position advertised on 3 job boards</p>
          <p>Phone screen prospective candidates and conduct up to 3 in-person interviews based on position specific requirements</p>
          <p>Client will be presented with a summarization of the interviews, based on a candidate ranking system, as well as the prospective candidates resume</p>
        </section>
      </div>

      <section class="package package-d">
        <div class="package-tab">Package D<span class="sep">|</span>Percentage of Prospective Candidates Annual Salary</div>
        <p>Recruiter will take the time to learn about your organization so they can identify individuals with qualities that will best match with your team. They will source, conduct in-depth interviews via phone and in-person, as well as perform thorough background and reference checks prior to employment.</p>
        <p>Package also included:</p>
        <p>Create a customized job description that best fits your organizations needs</p>
        <p>Position advertised on 3 job boards</p>
        <p>Client will be presented with a summarization of the interviews, based on a candidate ranking system, as well as the prospective candidates resume</p>
      </section>
    </div>

    <footer class="footer">
      <span class="footer-item">Suite 4, 120 Harbour Road Northgate 5012</span>
      <span class="footer-item">
        <svg viewBox="0 0 12 12"><circle cx="6" cy="6" r="6" fill="#2f6db5"/><path d="M4 3.2l1 1.4-.6.8c.4.8 1 1.4 1.8 1.8l.8-.6 1.4 1-.5 1.2C5.8 8.6 3.4 6.2 3.2 4z" fill="#fff"/></svg>
        08 5550 1234
      </span>
      <span class="footer-item">
        <svg viewBox="0 0 12 12"><circle cx="6" cy="6" r="6" fill="#2f6db5"/><rect x="3" y="4" width="6" height="4.2" fill="none" stroke="#fff" stroke-width=".9"/><path d="M3 4l3 2.4L9 4" fill="none" stroke="#fff" stroke-width=".9"/></svg>
        hello@brightwayhr.example
      </span>
      <span class="footer-item">
        <svg viewBox="0 0 12 12"><circle cx="6" cy="6" r="6" fill="#2f6db5"/><circle cx="6" cy="6" r="3" fill="none" stroke="#fff" stroke-width=".9"/><path d="M3 6h6M6 3v6" stroke="#fff" stroke-width=".7"/></svg>
        www.brightwayhr.example
      </span>
    </footer>
  </div>
</body>
</html>
```